New Stationery New Logo for KT Fabrication Limited

We have a new logo and now want new stationary to go with it

This will be

Letterhead
Compliments Slip
Business Cards

Company details are
KT Fabrication Limited
Dellmoor Road, Rugby, Warwickshire, CV34 7HX, UK
Telephone : +44(0)1788 390617
Fax: +44(0)1788 473928
Email: sales@ktfabrication.co.uk
Web: www.ktfabrication.co.uk

Target Market(s)

Engineering / Metal Stamping

Industry/Entity Type

Manufacture

Contact Information for Business Card

Colin Brearley
Business Development Manager
KT Fabrication Limited
Dellmoor Road
Rugby
Warwickshire
CV34 7HX, UK

T: +44(0)1788 390617
F: +44(0)1788 473928
E: sales@ktfabrication.co.uk
W: www.ktfabrication.co.uk

Font styles to use
Sans Serif

Colors
33a6d7
0555a3
3176b5
85cae6
85acd3

Requirements
Must have
• Logo

```html
<!DOCTYPE html>
<html lang="en">
<head>
<meta charset="utf-8">
<title>KT Fabrication Stationery</title>
<link rel="stylesheet" href="https://fonts.googleapis.com/css2?family=Montserrat:wght@400;500;600&family=Open+Sans:wght@400;600&family=Dancing+Script:wght@500&display=swap">
<style>
  :root {
    --navy: #0555a3;
    --deep: #15468a;
    --mid: #3176b5;
    --sky: #85cae6;
    --soft: #85acd3;
    --paper: #ffffff;
    --ink: #4a4f57;
    --ground: #eceef1;
  }
  * { margin: 0; padding: 0; box-sizing: border-box; }
  html, body { width: 1200px; height: 795px; overflow: hidden; background: var(--ground); }
  body { position: relative; font-family: "Open Sans", sans-serif; color: var(--ink); }

  .sheet { position: absolute; background: var(--paper); box-shadow: 0 2px 6px rgba(0,0,0,.12); }
  .rule-top { position: absolute; top: 0; left: 0; right: 0; height: 3px; background: var(--navy); }

  .brand { display: flex; align-items: center; gap: 6px; font-family: "Montserrat", sans-serif; font-weight: 500; letter-spacing: .28em; color: var(--navy); white-space: nowrap; }
  .brand-dot { width: 1em; height: 1em; border-radius: 50%; background: var(--mid); flex: none; }
  .brand.on-blue { color: #fff; }
  .brand.on-blue .brand-dot { background: var(--sky); }

  .details { font-size: 5.5px; line-height: 8px; color: var(--ink); border-left: 1px solid var(--soft); padding-left: 6px; }
  .details .label { color: var(--navy); display: inline-block; width: 26px; font-weight: 600; }
  .details .company { color: var(--navy); }
  .web { position: absolute; font-size: 6px; color: var(--navy); border-left: 1px solid var(--soft); padding-left: 6px; }

  /* Letterhead */
  .letterhead { left: 470px; top: 40px; width: 340px; height: 481px; }
  .letterhead .brand { position: absolute; left: 30px; top: 32px; font-size: 10px; }
  .letterhead .details { position: absolute; left: 200px; top: 26px; }
  .letter-body { position: absolute; left: 30px; top: 92px; width: 280px; font-size: 5.6px; line-height: 8.4px; }
  .letter-body .greeting { font-weight: 600; margin-bottom: 7px; }
  .letter-body p { margin-bottom: 7px; }
  .signature { font-family: "Dancing Script", cursive; font-size: 17px; color: #222; margin-top: 10px; line-height: 20px; }
  .sign-role { font-weight: 600; font-size: 5.6px; }
  .letterhead .web { right: 30px; bottom: 28px; }

  /* Compliments slip */
  .slip { left: 835px; top: 330px; width: 340px; height: 160px; }
  .slip-title { position: absolute; right: 22px; top: 20px; font-family: "Montserrat", sans-serif; font-weight: 400; font-size: 11px; color: var(--navy); letter-spacing: .02em; }
  .slip .web { right: 22px; top: 40px; }
  .slip .brand { position: absolute; left: 22px; top: 68px; font-size: 9px; }
  .slip .details { position: absolute; left: 22px; top: 96px; }

  /* Business cards */
  .card { width: 210px; height: 120px; }
  .card-front { left: 40px; top: 60px; background: var(--deep); }
  .card-front .brand { position: absolute; left: 0; right: 0; top: 46px; justify-content: center; font-size: 10px; }
  .card-front .card-web { position: absolute; left: 0; right: 0; top: 66px; text-align: center; font-size: 5.5px; color: var(--sky); }
  .card-back { left: 40px; top: 200px; }
  .card-back .brand { position: absolute; right: 14px; top: 14px; font-size: 6.5px; }
  .card-person { position: absolute; left: 16px; top: 40px; }
  .card-person .name { font-family: "Montserrat", sans-serif; font-weight: 500; font-size: 7.5px; color: var(--navy); letter-spacing: .04em; }
  .card-person .role { font-size: 5px; margin-bottom: 5px; }
  .card-person .details { font-size: 5px; line-height: 7px; }
  .card-person .details .label { width: 22px; }

  /* Notebook */
  .notebook { left: 130px; top: 350px; width: 270px; height: 380px; background: var(--deep); }
  .spiral { position: absolute; left: 4px; top: 10px; }
  .notebook .brand { position: absolute; left: 0; right: 0; top: 170px; justify-content: center; font-size: 13px; }
  .notebook .cover-web { position: absolute; left: 0; right: 0; top: 196px; text-align: center; font-size: 7px; color: var(--sky); }
</style>
</head>
<body>

  <!-- Letterhead -->
  <section class="sheet letterhead">
    <div class="rule-top"></div>
    <div class="brand"><span class="brand-dot"></span>KT FABRICATION</div>
    <div class="details">
      <div class="company">KT Fabrication Limited</div>
      <div>Dellmoor Road, Rugby</div>
      <div>Warwickshire, CV34 7HX, UK</div>
      <div><span class="label">PHONE</span>+44(0)1788 390617</div>
      <div><span class="label">FAX</span>+44(0)1788 473928</div>
      <div><span class="label">EMAIL</span>sales@ktfabrication.co.uk</div>
    </div>
    <div class="letter-body">
      <div class="greeting">Lorem ipsum,</div>
      <p>Cras mattis consectetur purus sit amet fermentum. Etiam porta sem malesuada magna mollis euismod. Integer posuere erat a ante venenatis dapibus posuere velit aliquet. Cras justo odio, dapibus ac facilisis in, egestas eget quam. Aenean eu leo quam.</p>
      <p>Vivamus sagittis lacus vel augue laoreet rutrum faucibus dolor auctor. Donec sed odio dui. Nullam quis risus eget urna mollis ornare vel eu leo. Maecenas faucibus mollis interdum.</p>
      <p>Donec id elit non mi porta gravida at eget metus. Fusce dapibus, tellus ac cursus commodo, tortor mauris condimentum nibh, ut fermentum massa justo sit amet risus.</p>
      <p>Cum sociis natoque penatibus et magnis dis parturient montes, nascetur ridiculus mus. Sed posuere consectetur est at lobortis.</p>
      <p>Cras justo odio, dapibus ac facilisis in, egestas eget quam. Morbi leo risus, porta ac consectetur ac, vestibulum at eros.</p>
      <div class="signature">Your Name</div>
      <div class="sign-role">Company Director</div>
    </div>
    <div class="web">www.ktfabrication.co.uk</div>
  </section>

  <!-- Business card front -->
  <section class="sheet card card-front">
    <div class="brand on-blue"><span class="brand-dot"></span>KT FABRICATION</div>
    <div class="card-web">www.ktfabrication.co.uk</div>
  </section>

  <!-- Business card back -->
  <section class="sheet card card-back">
    <div class="brand"><span class="brand-dot"></span>KT FABRICATION</div>
    <div class="card-person">
      <div class="name">COLIN BREARLEY</div>
      <div class="role">Business Development Manager</div>
      <div class="details">
        <div><span class="label">PHONE</span>+44(0)1788 390617</div>
        <div><span class="label">FAX</span>+44(0)1788 473928</div>
        <div><span class="label">EMAIL</span>sales@ktfabrication.co.uk</div>
        <div class="company">KT Fabrication Limited</div>
        <div>Dellmoor Road, Rugby</div>
        <div>Warwickshire, CV34 7HX, UK</div>
      </div>
    </div>
  </section>

  <!-- Notebook -->
  <section class="sheet notebook">
    <svg class="spiral" width="10" height="360" viewBox="0 0 10 360" aria-hidden="true">
      <defs>
        <pattern id="coil" width="10" height="14" patternUnits="userSpaceOnUse">
          <circle cx="5" cy="7" r="3" fill="none" stroke="#8a8f98" stroke-width="1.4"/>
        </pattern>
      </defs>
      <rect width="10" height="360" fill="url(#coil)"/>
    </svg>
    <div class="brand on-blue"><span class="brand-dot"></span>KT FABRICATION</div>
    <div class="cover-web">www.ktfabrication.co.uk</div>
  </section>

  <!-- Compliments slip -->
  <section class="sheet slip">
    <div class="rule-top"></div>
    <div class="slip-title">WITH COMPLIMENTS</div>
    <div class="web">www.ktfabrication.co.uk</div>
    <div class="brand"><span class="brand-dot"></span>KT FABRICATION</div>
    <div class="details">
      <div class="company">KT Fabrication Limited</div>
      <div>Dellmoor Road, Rugby</div>
      <div>Warwickshire, CV34 7HX, UK</div>
      <div><span class="label">PHONE</span>+44(0)1788 390617</div>
      <div><span class="label">FAX</span>+44(0)1788 473928</div>
      <div><span class="label">EMAIL</span>sales@ktfabrication.co.uk</div>
    </div>
  </section>

</body>
</html>
```